halbrook paving works

Needs to have phone number 0418352790 and email carlwhitby@mailnest.com.au.
ABN 27813046652
name carl whitby

For all your concreting solutions
Excavation
Exposed & colour concrete
House & shed slabs
Driveways
Landing & steps

Contact Information for Business Card

ph 0418352790
email carlwhitby@mailnest.com.au.
ABN 27813046652
name carl whitby

```html
<!DOCTYPE html>
<html lang="en">
<head>
<meta charset="utf-8">
<title>Halbrook Paving Works – Business Card</title>
<link href="https://fonts.googleapis.com/css2?family=Lato:wght@400;700&family=Montserrat:wght@500;600&display=swap" rel="stylesheet">
<style>
  :root {
    --bg: #2a2a2b;
    --card: #1e1e1f;
    --card-edge: #161617;
    --orange: #f36a21;
    --white: #f4f4f4;
    --pattern-dark: #1a1a1b;
    --pattern-light: #3a3a3c;
  }
  * { margin: 0; padding: 0; box-sizing: border-box; }
  html, body { width: 1200px; height: 900px; overflow: hidden; }
  body { background: var(--bg); font-family: "Lato", sans-serif; position: relative; }

  .card {
    position: absolute; left: 290px; width: 620px; height: 378px;
    background: var(--card); border: 1px solid var(--card-edge);
    box-shadow: 0 14px 30px rgba(0,0,0,.45);
  }
  .card--back { top: 56px; }
  .card--front { top: 468px; }

  .back-texture {
    position: absolute; inset: 0;
    background: linear-gradient(135deg, var(--pattern-dark) 0%, #252527 45%, var(--pattern-light) 100%);
  }
  .back-mark {
    position: absolute; left: 400px; top: 208px;
    display: flex; align-items: center; gap: 8px;
  }
  .mark-square {
    width: 22px; height: 22px; background: var(--orange);
    transform: rotate(45deg); flex: none;
  }
  .back-mark .mark-name {
    font-family: "Montserrat", sans-serif; font-weight: 600;
    font-size: 10px; letter-spacing: .5px; color: var(--white);
  }

  .brand {
    position: absolute; left: 40px; top: 139px;
    display: flex; align-items: center; gap: 16px;
  }
  .brand .mark-square { width: 44px; height: 44px; margin: 0 10px; }
  .brand-rule { width: 2px; height: 68px; background: var(--orange); }
  .brand-text { display: flex; flex-direction: column; align-items: center; gap: 3px; width: 140px; }
  .brand-name {
    font-family: "Montserrat", sans-serif; font-weight: 600;
    font-size: 13px; color: var(--orange); letter-spacing: .2px; white-space: nowrap;
  }
  .brand-sub {
    display: flex; align-items: center; gap: 6px; width: 100%;
    font-family: "Montserrat", sans-serif; font-weight: 500;
    font-size: 10px; color: var(--white); letter-spacing: 3px;
  }
  .brand-sub::before, .brand-sub::after { content: ""; flex: 1; height: 1px; background: var(--white); }
  .brand-phone {
    font-family: "Montserrat", sans-serif; font-weight: 500;
    font-size: 10px; color: var(--orange); letter-spacing: 2px;
  }

  .divider {
    position: absolute; left: 316px; top: 124px;
    width: 2px; height: 190px; background: var(--orange);
  }

  .details { position: absolute; left: 342px; top: 124px; color: var(--white); }
  .person-name {
    font-family: "Montserrat", sans-serif; font-weight: 500;
    font-size: 27px; color: var(--orange); letter-spacing: 1px; line-height: 1;
  }
  .person-role { font-size: 15px; margin-top: 4px; }
  .location { margin-top: 10px; font-size: 15px; line-height: 1.3; }
  .location .suburb { color: var(--orange); }
  .contact-list { list-style: none; margin-top: 8px; font-size: 15px; }
  .contact-list li { display: flex; align-items: center; gap: 9px; line-height: 1.5; }
  .contact-list svg { width: 11px; height: 11px; flex: none; }
  .accent { color: var(--orange); }
  .abn-label { color: var(--orange); font-weight: 700; font-size: 10px; width: 11px; }
</style>
</head>
<body>

<section class="card card--back" aria-label="Business card back">
  <div class="back-texture" role="img" aria-label="Embossed diagonal lattice pattern in dark grey"></div>
  <div class="back-mark">
    <span class="mark-square"></span>
    <span class="mark-name">HALBROOK PAVING WORKS</span>
  </div>
</section>

<section class="card card--front" aria-label="Business card front">
  <div class="brand">
    <span class="mark-square"></span>
    <span class="brand-rule"></span>
    <div class="brand-text">
      <span class="brand-name">HALBROOK PAVING</span>
      <span class="brand-sub">WORKS</span>
      <span class="brand-phone">0418352790</span>
    </div>
  </div>

  <div class="divider"></div>

  <div class="details">
    <h1 class="person-name">CARL WHITBY</h1>
    <p class="person-role">Director</p>
    <p class="location"><span class="suburb">Marrow Creek</span><br>Dunmore, Tasmania 7041</p>
    <ul class="contact-list">
      <li>
        <svg viewBox="0 0 12 12"><path fill="var(--orange)" d="M2.5 1l2 2.2-1 1.3c.7 1.5 1.8 2.6 3.2 3.3l1.3-1 2 2-1 1.2C5 9.6 2.4 7 1.2 2.1z"/></svg>
        +61 418 352 790
      </li>
      <li>
        <svg viewBox="0 0 12 12"><rect x="1" y="2.5" width="10" height="7" fill="none" stroke="var(--orange)" stroke-width="1.2"/><path d="M1 2.5l5 4 5-4" fill="none" stroke="var(--orange)" stroke-width="1.2"/></svg>
        carlwhitby@mailnest.com.au
      </li>
      <li>
        <svg viewBox="0 0 12 12"><circle cx="6" cy="6" r="5" fill="none" stroke="var(--orange)" stroke-width="1.1"/><path d="M1 6h10M6 1c-2.4 3-2.4 7 0 10M6 1c2.4 3 2.4 7 0 10" fill="none" stroke="var(--orange)" stroke-width="1"/></svg>
        <span>www.<span class="accent">halbrookpaving</span>.com.au</span>
      </li>
      <li>
        <svg viewBox="0 0 12 12"><rect x="1.5" y="1.5" width="9" height="9" fill="none" stroke="var(--orange)" stroke-width="1.2"/></svg>
        <span><span class="accent">ABN</span> 27813046652</span>
      </li>
    </ul>
  </div>
</section>

</body>
</html>
```